Business Card Design

Vintage looking Hair Salon, where the customer service is 100%. We are based in a cottage. With shabby chic console tables and beautiful ornate mirrors..and rich brown leather cutting chairs. Chandeliers at the window, and a ornate patchwork sofa.
our clientele are 28years upwards.. Mums with small children.. Ladies that lunch, and men that want more than a barbers and are prepared to pay for our services.
I am looking for a classy business card.. That look expensive.. Where our initials WHP become a visual reference.. I was thinking of cream card initials in black on a embossed tarnished silver.. But I'm open to suggestion. I want,  need the design to be able to work with flyers price list ect.

Willowmere Hair Parlour
27 Fenwick Row
Ardley Green
bN42 6TW
FB thewillowmerehairparlour
Info@thewillowmerhairparlour.co.uk
0208 715 2964

```html
<!DOCTYPE html>
<html lang="en">
<head>
<meta charset="utf-8">
<title>Willowmere Hair Parlour – Business Card</title>
<link rel="stylesheet" href="https://fonts.googleapis.com/css2?family=Marcellus&family=Lato:wght@400&display=swap">
<style>
  :root {
    --backdrop: #cbbfa9;
    --card: #ffffff;
    --ink: #6e6e6e;
    --ink-soft: #858585;
    --silver-dark: #8e8e8e;
    --silver-mid: #b9b9b9;
    --silver-light: #ececec;
    --silver-pale: #e2e2e2;
    --divider: #9a9a9a;
  }
  * { margin: 0; padding: 0; box-sizing: border-box; }
  html, body { width: 1200px; height: 880px; overflow: hidden; }
  body {
    background: var(--backdrop);
    display: flex;
    align-items: center;
    justify-content: center;
  }
  .business-card {
    position: relative;
    width: 1000px;
    height: 571px;
    background: var(--card);
    box-shadow: 0 6px 18px rgba(0,0,0,0.18);
    overflow: hidden;
  }
  .silver-sweep {
    position: absolute;
    top: 0; left: 0;
    width: 1000px;
    height: 260px;
  }
  .scissors-art {
    position: absolute;
    left: 600px;
    top: 70px;
    width: 270px;
    height: 170px;
    border-radius: 8px;
    background: linear-gradient(135deg, var(--silver-mid), var(--silver-pale));
    opacity: 0.85;
  }
  .flourish-art {
    position: absolute;
    left: 14px;
    top: 170px;
    width: 80px;
    height: 120px;
    border-radius: 6px;
    background: linear-gradient(180deg, var(--silver-pale), var(--silver-light));
  }
  .salon-name {
    position: absolute;
    left: 70px;
    top: 390px;
    font-family: "Marcellus", serif;
    font-weight: 400;
    color: var(--ink);
  }
  .salon-name .name-main {
    display: block;
    font-size: 50px;
    letter-spacing: 1px;
    line-height: 1;
  }
  .salon-name .name-sub {
    display: block;
    font-size: 30px;
    letter-spacing: 1px;
    margin-top: 8px;
    text-align: right;
    padding-right: 60px;
    line-height: 1;
  }
  .divider {
    position: absolute;
    left: 505px;
    top: 330px;
    width: 2px;
    height: 200px;
    background: var(--divider);
  }
  .contact-details {
    position: absolute;
    left: 528px;
    top: 330px;
    font-family: "Lato", sans-serif;
    font-size: 20px;
    line-height: 1.55;
    color: var(--ink-soft);
    list-style: none;
  }
</style>
</head>
<body>
  <article class="business-card">
    <svg class="silver-sweep" viewBox="0 0 1000 260" aria-hidden="true">
      <defs>
        <linearGradient id="silverGradient" x1="0" y1="1" x2="1" y2="0">
          <stop offset="0" stop-color="#ececec"/>
          <stop offset="0.55" stop-color="#b9b9b9"/>
          <stop offset="1" stop-color="#8e8e8e"/>
        </linearGradient>
      </defs>
      <path d="M0 150 C 220 120, 480 40, 760 0 L 1000 0 L 1000 30 C 880 80, 760 150, 620 210 C 540 170, 360 150, 0 175 Z" fill="url(#silverGradient)"/>
    </svg>
    <div class="flourish-art" role="img" aria-label="Silver ornamental flourish curling from the left edge"></div>
    <div class="scissors-art" role="img" aria-label="Silver salon scissors cutting the hair strands"></div>

    <h1 class="salon-name">
      <span class="name-main">The Willowmere</span>
      <span class="name-sub">Hair Parlour</span>
    </h1>

    <div class="divider"></div>

    <ul class="contact-details">
      <li>27 Fenwick Row, Ardley Green, BN42 6TW.</li>
      <li>PH : 0208 715 2964</li>
      <li>E : info@thewillowmerhairparlour.co.uk</li>
      <li>FB : thewillowmerehairparlour</li>
    </ul>
  </article>
</body>
</html>
```